Professional "Aviation Parts" Auction Website with Customer Login Backend Module

Need an "Aviation Parts" Website with 4 major listing options.
- AUCTION
Seller can list their items on the site as an auction with a small listing fee. Seller has to create an account in order to be able to create or edit a listing. Seller must be able to have a reserve price.
- SELLING
Sellers can list their items with a small listing fee. Imortant is, that Sellers has a back end module, (like trovix) where they can log in and create or make changes to existing listings.
- BUYING
Buyers can search items either by part number in a search bar, or scroll through categories and subcategories to find the respective part.
- WANTED
Customers should be able to create a “Wanted” listing for items of interest.

In all four cases, customers (Buyers/Seller) must create an account to either place a bid, buy now, create a “wanted” listing or create/edit their own for sale/auction listing. NO login is required to search the website or browse through categories and to see listings. The website should be “Trovix like” with login module, payment, coindrop connection, etc and easy to navigate. A design example is https://www.quellmarket-hub.com/ . I’m open for all ideas.

Target Market(s)

Aviation Industry
Helicopter Industry

Industry/Entity Type

Aviation

Number of Pages Required

5+ page

Font styles to use
Serif
Sans Serif

Colors
85acd3
3176b5
9d9d9d
d3d3d3

Requirements
Must have
• Our company is called Brelvox.com, LLC and is specialized in aviation parts listings. The website must have 4 major options: Auction, Sell, Buy, and Wanted listings. The Buyer/Seller must create an account in order to bid, buy or sell an item. No login is required if someone just wants to browse the website to look for pricing and parts. Once they decide to purchase, they have to login or create an account. The same counts for the seller. Seller must create an account to list a "For Sale", "Auction" or "Wanted" Listing. Each listing requires a small listing fee, which will be charged by us and should be paid via CoinDrop. CoinDrop should be interfaced as a preferred payment method. Other payment options are available as well. The website idea is very similar to Trovix. Same style listings as Trovix and other auction pages. A good design idea is https://www.quellmarket-hub.com/ to get a better understanding. The website must be easy to navigate and modern looking with a professional color scheme. The logo is attached. I would like to keep the website in a similar color scheme as the logo design.
• There should be two main Categories on the main page to select from:
• - Helicopter Listings
• - Airplane Listings
• The 1st "Sub-Category" once you click on either one of the top category, will be "Aircraft Make".
• The 2nd "Sub-Category" will be "Aircraft Model".
• The 3rd "Sub-Category" will be "Parts" for that specific aircraft.
• Also there should be a CoinDrop interface, if a buyer wants to purchase an item, so they can use their credit card or request wire information from the seller after closing.
• It also has to include an option when a seller lists an item, they will be required to make a payment to us for listing on our website. For example $1.99 for a listing value up to $100. A listing fee for a sale value of up to $1,000 will be $4.99, and so on. Listing fee for up to $10,000 will be $14.99. Listing fee for up to $100.000 will be $49.99. This system is very similar to the Trovix platform.
Nice to have
• It would be nice to have a easy to maintain back-end module which can easily be manged by our personnel.
Should not have
• The page should not look childish with random colors. A professional appearance and easy to navigate is a must.

```html
<!DOCTYPE html>
<html lang="en">
<head>
<meta charset="utf-8">
<title>Brelvox – Aviation Parts</title>
<link rel="stylesheet" href="https://fonts.googleapis.com/css2?family=Lato:wght@400;700;900&family=Roboto:wght@400;500;700&display=swap">
<style>
:root{
  --blue:#3176b5;
  --blue-dark:#2a63a0;
  --sky:#85acd3;
  --navy:#0d2c55;
  --orange:#df6420;
  --ink:#222;
  --grey:#9d9d9d;
  --light:#d3d3d3;
  --paper:#f6f7f9;
  --white:#fff;
  --footer-text:#dfe6ee;
}
*{box-sizing:border-box;margin:0;padding:0}
html,body{width:1200px;height:3072px;overflow:hidden}
body{font-family:'Roboto',Arial,sans-serif;color:var(--ink);background:#fff;position:relative}
.abs{position:absolute}
.topbar{top:0;left:0;width:1200px;height:40px;background:var(--blue);color:var(--white);font-size:13px;font-weight:500;display:flex;align-items:center;justify-content:space-between;padding:0 100px}
.topbar span{margin-right:18px}
.header{top:40px;left:0;width:1200px;height:98px;background:#fff;display:flex;align-items:center;padding:0 100px;justify-content:space-between}
.brand{display:flex;align-items:center;gap:10px;font-family:'Lato',sans-serif;font-weight:700;font-size:22px;color:var(--blue)}
.brand i{width:30px;height:30px;border-radius:50%;background:var(--blue);display:block}
.nav{display:flex;align-items:center;gap:28px;font-family:'Lato',sans-serif;font-weight:700;font-size:14px;color:#222}
.nav .on{color:var(--blue)}
.nav .search{width:38px;height:38px;border-radius:50%;background:#555;display:flex;align-items:center;justify-content:center}
.hero{top:138px;left:0;width:1200px;height:520px;background:#121212}
.hero-img{top:138px;left:0;width:640px;height:520px;background:radial-gradient(ellipse at 45% 50%,#9aa0a6 0%,#4c5156 40%,#151515 80%)}
.hero-title{top:275px;left:693px;font-family:'Lato',sans-serif;font-weight:900;font-size:50px;color:var(--white);letter-spacing:1px}
.hero-text{top:368px;left:693px;width:420px;color:var(--white);font-family:'Lato',sans-serif;font-size:16px;line-height:29px}
.btn-orange{background:var(--orange);color:var(--white);font-family:'Lato',sans-serif;font-weight:700;font-size:15px;display:flex;align-items:center;justify-content:center;border-radius:2px}
.arrow{top:383px;width:24px;height:24px;color:var(--white);font-size:24px}
.finder{top:658px;left:0;width:1200px;height:346px;background:linear-gradient(180deg,#3a7fc0,var(--blue))}
.tabs{top:722px;left:0;width:1200px;display:flex;justify-content:center;gap:32px;font-family:'Lato',sans-serif;font-weight:700;font-size:29px;color:var(--white);letter-spacing:1px}
.tabs .on{border-bottom:3px solid #fff;padding:0 10px 4px}
.select{top:815px;width:277px;height:43px;background:#fff;color:#777;font-size:13px;display:flex;align-items:center;justify-content:space-between;padding:0 18px}
.chev{top:974px;left:570px;width:60px;height:60px;border-radius:50%;background:#fff;box-shadow:0 2px 6px rgba(0,0,0,.15);display:flex;align-items:center;justify-content:center}
.side{top:1100px;left:100px;width:238px;height:355px;border:1px solid #e2e2e2;background:#fff}
.side h3{height:45px;background:var(--sky);color:var(--white);font-family:'Lato',sans-serif;font-weight:700;font-size:15px;display:flex;align-items:center;padding-left:28px}
.side ul{list-style:none;padding:14px 0 0 30px}
.side li{font-family:'Lato',sans-serif;font-size:14px;height:27.5px;display:flex;align-items:center;gap:10px;color:#333}
.side li b{width:12px;height:12px;border-radius:50%;background:var(--navy);display:inline-block}
.card{top:1100px;width:239px;text-align:center;font-family:'Lato',sans-serif}
.ph{height:236px;border:1px solid #ddd}
.card h4{font-size:17px;font-weight:700;margin-top:22px}
.price{color:var(--orange);font-size:21px;font-weight:700;margin-top:10px}
.pair{display:flex;justify-content:center;gap:12px;margin-top:10px}
.pair span{width:80px;height:24px;font-size:12px;display:flex;align-items:center;justify-content:center;border:1px solid var(--blue)}
.buy{background:var(--blue-dark);color:var(--white)}
.bid{color:var(--blue);background:#fff}
.wanted-bg{top:1540px;left:0;width:1200px;height:595px;background:linear-gradient(180deg,#fff,var(--paper))}
.sec-title{left:0;width:1200px;text-align:center;font-family:'Lato',sans-serif;font-weight:900;font-size:29px;color:#111}
.jet{top:1690px;left:40px;width:1160px;height:340px;background:linear-gradient(90deg,rgba(230,234,238,0),#eceff2 30%,#e8ecef 80%,rgba(230,234,238,0));border-radius:40% 10% 10% 40%}
.gear{top:1700px;left:100px;width:390px;height:340px;background:radial-gradient(circle at 50% 60%,#3a3a3a 0%,#1c1c1c 35%,rgba(230,234,238,0) 62%)}
.details{top:1720px;left:648px;width:452px;font-family:'Lato',sans-serif}
.details h3{font-size:23px;font-weight:900;color:#111}
.details h5{font-size:17px;font-weight:700;color:var(--blue);margin-top:24px}
.row{font-size:12px;color:#555;margin-top:13px;display:flex;white-space:nowrap}
.row em{font-style:normal;width:110px;flex:none}
.expert{font-size:13px;font-weight:700;color:var(--blue);margin-top:22px}
.call{display:flex;justify-content:space-between;font-size:12px;color:#555;margin-top:40px}
.call a{color:var(--blue);text-decoration:none;font-weight:700}
.sell{top:2308px;width:239px;text-align:center;font-family:'Lato',sans-serif}
.sell .ph{height:200px}
.sell h4{font-size:17px;font-weight:700;margin-top:24px}
.viewall{top:2598px;left:492px;width:216px;height:47px;border:2px solid var(--orange);color:var(--orange);font-family:'Lato',sans-serif;font-weight:700;font-size:13px;display:flex;align-items:center;justify-content:center;border-radius:3px;background:#fff}
.footer{top:2740px;left:0;width:1200px;height:332px;background:var(--navy)}
.info{left:100px;display:flex;gap:18px;font-size:13px;line-height:19px;color:var(--footer-text)}
.info svg{flex:none;margin-top:2px}
.flinks{top:2805px;left:540px;display:flex;gap:38px;font-size:12px;font-weight:500;color:var(--white)}
.fbrand{top:2880px;left:0;width:1200px;display:flex;flex-direction:column;align-items:center;gap:8px;font-family:'Lato',sans-serif;font-weight:700;font-size:22px;letter-spacing:2px;color:var(--white)}
.fbrand i{width:44px;height:44px;border-radius:50%;background:#fff;display:block}
.follow{top:2862px;left:847px;font-family:'Lato',sans-serif;font-weight:700;font-size:20px;letter-spacing:1px;color:var(--white)}
.socials{top:2910px;left:845px;display:flex;gap:10px}
.socials i{width:38px;height:38px;border:2px solid #fff;border-radius:50%;display:block}
.rule{top:3000px;left:100px;width:1000px;height:1px;background:rgba(255,255,255,.3)}
.copy{top:3030px;left:100px;font-size:13px;color:var(--footer-text)}
.pay{top:3024px;left:893px;display:flex;gap:6px}
.pay i{width:46px;height:28px;background:#fff;border-radius:3px;display:block}
.code{top:3032px;left:1146px;font-size:12px;color:var(--footer-text)}
</style>
</head>
<body>

<div class="abs topbar">
  <div><span>&#9742; Sales:(+1) 555 010 4821</span><span>|</span><span>24/7 Technical Support</span></div>
  <div><span>Buyers Sign-Up</span><span>|</span><span>Seller Sign-Up</span><span>|</span><span>My Cart</span></div>
</div>

<header class="abs header">
  <div class="brand"><i></i>BRELVOX</div>
  <nav class="nav">
    <span class="on">HOME</span><span>ABOUT US</span><span>AUCTION</span><span>SELL</span><span>BUY</span><span>WANTED</span><span>NEWS</span><span>CONTACT</span>
    <span class="search"><svg width="16" height="16" viewBox="0 0 16 16"><circle cx="6.5" cy="6.5" r="5" stroke="#fff" stroke-width="2" fill="none"/><line x1="10" y1="10" x2="15" y2="15" stroke="#fff" stroke-width="2"/></svg></span>
  </nav>
</header>

<section class="abs hero"></section>
<div class="abs hero-img" role="img" aria-label="Turbofan aircraft engine on a stand"></div>
<div class="abs arrow" style="left:40px">&#8249;</div>
<div class="abs arrow" style="left:1146px">&#8250;</div>
<h1 class="abs hero-title">BRELVOX</h1>
<p class="abs hero-text">There are many variations of passages of Lorem Ipsum available but the majority have suffered.</p>
<div class="abs btn-orange" style="top:460px;left:693px;width:162px;height:47px">READ MORE &#10148;</div>

<section class="abs finder" role="img" aria-label="Faint aircraft silhouette behind the parts finder"></section>
<svg class="abs" style="top:690px;left:566px" width="68" height="24" viewBox="0 0 68 24"><path d="M2 12h64M34 2l6 10-6 10M28 12l-10-8M28 12l-10 8" stroke="#fff" stroke-width="2" fill="none"/></svg>
<div class="abs tabs"><span class="on">AIRPLANE</span><span>HELICOPTER</span></div>
<div class="abs select" style="left:158px">Aircraft Model<span>&#8964;</span></div>
<div class="abs select" style="left:460px">Aircraft Make<span>&#8964;</span></div>
<div class="abs select" style="left:762px">Parts<span>&#8964;</span></div>
<div class="abs btn-orange" style="top:890px;left:506px;width:186px;height:47px;font-size:14px">&#9906; SEARCH NOW</div>
<div class="abs chev"><svg width="22" height="22" viewBox="0 0 22 22"><path d="M4 4l7 7 7-7M4 11l7 7 7-7" stroke="#3176b5" stroke-width="2.5" fill="none"/></svg></div>

<aside class="abs side">
  <h3>AUCTION PRODUCTS</h3>
  <ul>
    <li><b></b>Windows</li><li><b></b>Interiors &amp; Trim</li><li><b></b>Safety &amp; Mission</li><li><b></b>Landing Gear</li><li><b></b>Composites</li><li><b></b>Doors &amp; Seating</li><li><b></b>Ground Handling</li><li><b></b>Lighting &amp; Vision</li><li><b></b>Fuel &amp; Filters</li><li><b></b>Floats &amp; Equipment</li>
  </ul>
</aside>
<div class="abs card" style="left:353px"><div class="ph" role="img" aria-label="Set of steel gears" style="background:linear-gradient(135deg,#c9c9c9,#6d6d6d)"></div><h4>Aviation Part Name</h4><div class="price">$428.00</div><div class="pair"><span class="buy">Buy Now</span><span class="bid">Bid Now</span></div></div>
<div class="abs card" style="left:608px"><div class="ph" role="img" aria-label="Jet engine interior" style="background:linear-gradient(135deg,#3d6a9a,#b8c3cc)"></div><h4>Aviation Part Name</h4><div class="price">$428.00</div><div class="pair"><span class="buy">Buy Now</span><span class="bid">Bid Now</span></div></div>
<div class="abs card" style="left:862px"><div class="ph" role="img" aria-label="Cutaway turbofan engine render" style="background:radial-gradient(circle,#3a3aa0,#555 45%,#fff 75%)"></div><h4>Aviation Part Name</h4><div class="price">$428.00</div><div class="pair"><span class="buy">Buy Now</span><span class="bid">Bid Now</span></div></div>

<div class="abs wanted-bg"></div>
<div class="abs jet" role="img" aria-label="Faint airliner in the background"></div>
<h2 class="abs sec-title" style="top:1620px">WANTED PRODUCTS</h2>
<div class="abs gear" role="img" aria-label="Landing gear wheel assembly"></div>
<div class="abs btn-orange" style="top:1863px;left:224px;width:158px;height:42px;font-size:15px">ENQUIRE NOW</div>
<div class="abs details">
  <h3>EQUIPMENT DETAILS</h3>
  <h5>Ground Handling Wheels</h5>
  <div class="row"><em>Product ID :</em>10676</div>
  <div class="row"><em>Category :</em>Landing Equipment</div>
  <div class="row"><em>Equipment Type :</em>Handling Wheels</div>
  <div class="row"><em>Usage History :</em>Refurbished</div>
  <div class="row"><em>Current State :</em>Functional - Disassembled Demonstrable</div>
  <div class="expert">Ask an Expert: Brelvox &#187;</div>
  <div class="call"><span>Call Us: +1 (555) 014-7730</span><span>Stay current on live : <a>Subscribe &gt;</a></span></div>
</div>

<h2 class="abs sec-title" style="top:2220px">SELLING PRODUCTS</h2>
<div class="abs sell" style="left:100px"><div class="ph" role="img" aria-label="Blue jet engine intake" style="background:radial-gradient(circle at 45% 50%,#222 0%,#2d5fb0 35%,#cfd9e6 75%)"></div><h4>Aviation Part Name</h4></div>
<div class="abs sell" style="left:353px"><div class="ph" role="img" aria-label="Part on a display stand" style="background:linear-gradient(180deg,#f2f2f2,#bdbdbd)"></div><h4>Aviation Part Name</h4></div>
<div class="abs btn-orange" style="top:2385px;left:417px;width:106px;height:38px;background:var(--blue-dark)">Buy Now</div>
<div class="abs sell" style="left:608px"><div class="ph" role="img" aria-label="Engine cutaway with red casing" style="background:linear-gradient(135deg,#b23030,#6b6b6b 50%,#2a2a2a)"></div><h4>Aviation Part Name</h4></div>
<div class="abs sell" style="left:862px"><div class="ph" role="img" aria-label="Turbine component on a workbench" style="background:linear-gradient(135deg,#8a8a8a,#2b2b2b)"></div><h4>Aviation Part Name</h4></div>
<div class="abs viewall">VIEW ALL PRODUCTS &#10148;</div>

<footer class="abs footer"></footer>
<div class="abs info" style="top:2800px"><svg width="16" height="16" viewBox="0 0 16 16"><circle cx="8" cy="8" r="7" stroke="#fff" stroke-width="2" fill="none"/><path d="M8 4v4h3" stroke="#fff" stroke-width="2" fill="none"/></svg><div>Market Hours:<br>Monday - Sat(9:00 AM - 9:00 PM)</div></div>
<div class="abs info" style="top:2860px"><svg width="16" height="16" viewBox="0 0 16 16"><path d="M3 1l3 3-2 2c1 2 3 4 5 5l2-2 3 3-2 3C6 14 2 10 1 3z" fill="#fff"/></svg><div>Phone Support:<br>(+1) 555 010 4821</div></div>
<div class="abs info" style="top:2920px"><svg width="16" height="14" viewBox="0 0 16 14"><rect x="1" y="2" width="14" height="10" fill="#fff"/><path d="M1 2l7 5 7-5" stroke="#0d2c55" stroke-width="1.5" fill="none"/></svg><div>Email Support:<br>support@brelvox.com</div></div>
<div class="abs flinks"><span>SEARCH</span><span>HOME</span><span>ABOUT US</span><span>PRODUCTS</span><span>NEWS &amp; UPDATES</span><span>CONTACT US</span></div>
<div class="abs fbrand"><i></i>BRELVOX</div>
<div class="abs follow">FOLLOW US</div>
<div class="abs socials"><i></i><i></i><i></i><i></i><i></i></div>
<div class="abs rule"></div>
<div class="abs copy">© Copyright 2018 Brelvox. All Rights Reserved &nbsp;|&nbsp; Privacy Policy.</div>
<div class="abs pay"><i></i><i></i><i></i><i></i></div>
<div class="abs code">C10</div>

</body>
</html>
```